Life Coaching Business - needs business card design with logo

I need a business card and logo design for a life coaching business I started based in Los Angeles. I offer services to clients that wish to bring more balance and overall wholeness to their lives. As of right now, the business name is "Marcus Elwood Coaching." An iidea I had for the logo was to be kind of a Yin-Yang symbol but with dolphins, as the dolphin has symbolic meaning for my business. Although I am really open to other ideas as long as it incorporates the idea of “balance,” “wholeness,” and “dolphins.”I also wanted to incorporate the color blue, maybe in the form of water, waves, or some sort of peaceful imagery.

```html
<!DOCTYPE html>
<html lang="en">
<head>
<meta charset="utf-8">
<title>Marcus Elwood Coaching – Business Card</title>
<link href="https://fonts.googleapis.com/css2?family=Marcellus&family=Questrial&display=swap" rel="stylesheet">
<style>
  :root {
    --teal: #2a879e;
    --teal-deep: #1f6f84;
    --ink: #2b2b2b;
    --paper: #ffffff;
    --backdrop: #1d1d1d;
  }
  html, body {
    margin: 0;
    width: 1200px;
    height: 895px;
    overflow: hidden;
    background: var(--backdrop);
  }
  .canvas {
    position: relative;
    width: 1200px;
    height: 895px;
  }
  .card {
    position: absolute;
    width: 540px;
    height: 310px;
    box-shadow: 0 14px 30px rgba(0,0,0,.55);
    box-sizing: border-box;
  }
  .card-front {
    left: 60px;
    top: 40px;
    background: var(--teal);
    display: flex;
    flex-direction: column;
    align-items: center;
    justify-content: center;
    gap: 14px;
  }
  .card-back {
    left: 620px;
    top: 300px;
    background: var(--paper);
  }
  .mark-circle {
    border-radius: 50%;
    box-sizing: border-box;
  }
  .card-front .mark-circle {
    width: 110px;
    height: 110px;
    border: 3px solid var(--paper);
  }

  /* Wordmark: stacked name with letterspaced sub-line between rules */
  .wordmark {
    display: inline-flex;
    flex-direction: column;
    align-items: stretch;
    font-family: "Marcellus", serif;
    font-weight: 400;
  }
  .brand-name {
    margin: 0;
    text-align: center;
    white-space: nowrap;
    line-height: 1;
  }
  .brand-sub {
    margin: 0;
    display: flex;
    align-items: center;
    gap: 8px;
    white-space: nowrap;
    line-height: 1;
  }
  .brand-sub .rule {
    flex: 1;
    height: 1px;
    background: currentColor;
  }
  .card-front .wordmark { color: var(--paper); }
  .card-front .brand-name { font-size: 36px; }
  .card-front .brand-sub { font-size: 11px; letter-spacing: 5px; margin-top: 2px; }

  .back-brand {
    position: absolute;
    right: 34px;
    top: 24px;
    display: flex;
    flex-direction: column;
    align-items: center;
    gap: 8px;
  }
  .back-brand .mark-circle {
    width: 76px;
    height: 76px;
    border: 2px solid var(--teal);
  }
  .back-brand .wordmark { color: var(--teal); }
  .back-brand .brand-name { font-size: 26px; }
  .back-brand .brand-sub { font-size: 9px; letter-spacing: 4px; margin-top: 2px; }

  .divider {
    position: absolute;
    left: 34px;
    right: 34px;
    top: 166px;
    height: 1px;
    background: var(--ink);
  }
  .address {
    position: absolute;
    right: 34px;
    top: 178px;
    text-align: right;
    font-family: "Questrial", sans-serif;
    font-size: 12.5px;
    line-height: 1.5;
    color: var(--ink);
  }
  .person {
    position: absolute;
    left: 34px;
    top: 182px;
    width: 230px;
  }
  .person-name {
    font-family: "Marcellus", serif;
    color: var(--teal);
    font-size: 22px;
    margin: 0;
    letter-spacing: .5px;
  }
  .person-title {
    font-family: "Questrial", sans-serif;
    font-size: 11px;
    color: var(--ink);
    margin: 2px 0 8px;
    letter-spacing: .5px;
  }
  .person-rule {
    height: 1px;
    background: var(--ink);
    margin-bottom: 8px;
  }
  .contacts {
    list-style: none;
    margin: 0;
    padding: 0;
    font-family: "Questrial", sans-serif;
    font-size: 11.5px;
    color: var(--ink);
  }
  .contacts li {
    display: flex;
    align-items: center;
    gap: 7px;
    margin-bottom: 4px;
    white-space: nowrap;
  }
  .contacts svg {
    width: 11px;
    height: 11px;
    flex: none;
    fill: var(--teal-deep);
  }

  .logo-lockup {
    position: absolute;
    left: 16px;
    top: 556px;
    width: 400px;
    display: flex;
    flex-direction: column;
    align-items: center;
    gap: 22px;
  }
  .logo-lockup .mark-circle {
    width: 210px;
    height: 210px;
    border: 6px solid var(--teal-deep);
  }
  .logo-lockup .wordmark { color: var(--teal); }
  .logo-lockup .brand-name { font-size: 54px; }
  .logo-lockup .brand-sub { font-size: 20px; letter-spacing: 9px; margin-top: 4px; }
</style>
</head>
<body>
<main class="canvas">
  <section class="card card-front" aria-label="Card front">
    <div class="mark-circle"></div>
    <div class="wordmark">
      <p class="brand-name">Marcus Elwood</p>
      <p class="brand-sub"><span class="rule"></span>Coaching<span class="rule"></span></p>
    </div>
  </section>

  <section class="card card-back" aria-label="Card back">
    <div class="back-brand">
      <div class="mark-circle"></div>
      <div class="wordmark">
        <p class="brand-name">Marcus Elwood</p>
        <p class="brand-sub"><span class="rule"></span>Coaching<span class="rule"></span></p>
      </div>
    </div>
    <div class="divider"></div>
    <div class="address">
      4417 Ocean Park Blvd<br>
      Suite # B<br>
      Los Angeles, CA 90405
    </div>
    <div class="person">
      <p class="person-name">OWEN HARTLEY</p>
      <p class="person-title">PRESIDENT</p>
      <div class="person-rule"></div>
      <ul class="contacts">
        <li>
          <svg viewBox="0 0 24 24" aria-hidden="true"><path d="M6.6 10.8a15 15 0 0 0 6.6 6.6l2.2-2.2c.3-.3.7-.4 1-.2 1.1.4 2.3.6 3.6.6.6 0 1 .4 1 1V20c0 .6-.4 1-1 1A17 17 0 0 1 3 4c0-.6.4-1 1-1h3.5c.6 0 1 .4 1 1 0 1.3.2 2.5.6 3.6.1.3 0 .7-.2 1z"/></svg>
          310 555 0148
        </li>
        <li>
          <svg viewBox="0 0 24 24" aria-hidden="true"><path d="M2 5h20v14H2V5zm2 2v.5l8 5 8-5V7H4z"/></svg>
          hello@marcuselwoodcoaching.com
        </li>
        <li>
          <svg viewBox="0 0 24 24" aria-hidden="true"><path d="M12 2a10 10 0 1 0 0 20 10 10 0 0 0 0-20zm6.9 9h-3a15 15 0 0 0-1.3-6A8 8 0 0 1 18.9 11zM12 4c.9 1.2 1.7 3.8 1.9 7h-3.8C10.3 7.8 11.1 5.2 12 4zM9.4 5a15 15 0 0 0-1.3 6h-3A8 8 0 0 1 9.4 5zM5.1 13h3a15 15 0 0 0 1.3 6 8 8 0 0 1-4.3-6zM12 20c-.9-1.2-1.7-3.8-1.9-7h3.8c-.2 3.2-1 5.8-1.9 7zm2.6-1a15 15 0 0 0 1.3-6h3a8 8 0 0 1-4.3 6z"/></svg>
          www.marcuselwoodcoaching.com
        </li>
      </ul>
    </div>
  </section>

  <section class="logo-lockup" aria-label="Logo">
    <div class="mark-circle"></div>
    <div class="wordmark">
      <p class="brand-name">Marcus Elwood</p>
      <p class="brand-sub"><span class="rule"></span>Coaching<span class="rule"></span></p>
    </div>
  </section>
</main>
</body>
</html>
```